Fennick Medical - Flyer

We are a full service pharmacy that specializes in diabetic testing and medications. We research the patient's insurance to maximize their insurance benefit and then deliver the medications monthly directly to the patient's doorstep, for free! We save the patient, time and money every month.
We would love a flyer that we can distribute to Doctor's offices and patients that sum up our pharmacy. Emphasis on saving money, time, and getting the best quality supplies by maximizing their insurance. We want it to be eye catching, clean, and professional.
You can use our logo or feel free to make your own design.
diabetic patients wanting to save money
Insurance

```html
<!DOCTYPE html>
<html lang="en">
<head>
<meta charset="utf-8">
<title>Fennick Medical – Flyer</title>
<link href="https://fonts.googleapis.com/css2?family=Oswald:wght@400;500;600&family=Open+Sans:wght@400;600;700&display=swap" rel="stylesheet">
<style>
  :root{
    --green:#8cc63f;
    --green-dark:#6fa62a;
    --orange:#f58220;
    --charcoal:#3d3f42;
    --grey:#5b5d60;
    --paper:#ffffff;
    --stage:#e9e9e7;
  }
  *{box-sizing:border-box;margin:0;padding:0}
  html,body{width:1200px;height:1000px;overflow:hidden}
  body{background:var(--stage);font-family:"Open Sans",Arial,sans-serif;color:var(--grey);position:relative}
  .flyer{position:absolute;top:110px;width:540px;height:780px;background:var(--paper);overflow:hidden;box-shadow:0 6px 20px rgba(0,0,0,.18)}
  .flyer--front{left:45px}
  .flyer--back{left:615px}

  .hero-photo{position:absolute;left:0;top:0;width:100%;height:380px}
  .hero-photo--couple{background:linear-gradient(120deg,#d9d2c6 0%,#e8e2da 40%,#eef0ef 70%,#f4f5f4 100%)}
  .hero-photo--woman{background:linear-gradient(90deg,#ffffff 0%,#f3f3f2 45%,#e6dfd6 70%,#d8d0c5 100%)}
  .bands{position:absolute;left:0;width:100%;height:120px}
  .bands svg{display:block}

  .brand{position:absolute;display:flex;align-items:center;gap:8px;font-family:"Oswald",sans-serif;font-weight:500;color:var(--charcoal);letter-spacing:1px;text-transform:uppercase}
  .brand__mark{width:22px;height:22px;background:var(--green)}
  .brand__name{font-size:26px;line-height:1}

  .headline-save{position:absolute;right:28px;top:190px;width:230px;font-family:"Oswald",sans-serif;text-transform:uppercase;color:var(--charcoal)}
  .headline-save__big{font-size:52px;font-weight:600;color:var(--orange);line-height:1}
  .headline-save__sub{font-size:19px;font-weight:500;line-height:1.15}

  .intro{position:absolute;left:30px;top:410px;width:480px;font-family:"Oswald",sans-serif;font-weight:500;font-size:24px;line-height:1.2;color:var(--orange)}
  .photo-row{position:absolute;left:30px;top:490px;display:flex;gap:14px}
  .photo{width:233px;height:130px;border:3px solid #fff;box-shadow:0 1px 4px rgba(0,0,0,.25)}
  .photo--pharmacist{background:linear-gradient(135deg,#c9d5d8,#e9e4df 50%,#b7c6c9)}
  .photo--test{background:linear-gradient(135deg,#eef1f3,#d6dde2 60%,#9aa3a8)}
  .body-copy{position:absolute;left:30px;top:640px;width:480px;font-size:11.5px;line-height:1.55;color:var(--grey)}

  .footer{position:absolute;left:0;bottom:0;width:100%;height:56px;background:var(--green);display:flex;align-items:center;justify-content:space-between;padding:0 22px;color:#fff;font-size:13px;font-weight:600}
  .footer__item{display:flex;align-items:center;gap:6px}
  .footer svg{width:14px;height:14px;fill:#fff}

  .question{position:absolute;left:30px;top:110px;width:290px;font-family:"Oswald",sans-serif;text-transform:uppercase;color:var(--charcoal);line-height:1.05}
  .question__lead{font-size:21px;font-weight:500}
  .question__accent{font-size:21px;font-weight:500;color:var(--orange)}
  .question__big{font-size:40px;font-weight:600;color:var(--grey)}

  .gift-badge{position:absolute;right:6px;top:285px;width:130px;height:130px}

  .features{position:absolute;left:30px;top:420px;width:490px;list-style:none}
  .feature{display:flex;gap:18px;margin-bottom:14px}
  .feature__icon{flex:0 0 54px;height:54px;display:flex;align-items:center;justify-content:center}
  .feature__icon svg{width:50px;height:50px}
  .feature__title{font-family:"Oswald",sans-serif;font-weight:600;font-size:20px;text-transform:uppercase;color:var(--orange);line-height:1.1}
  .feature__title em{font-style:normal;color:var(--green-dark);text-transform:none}
  .feature__list{list-style:none;font-size:11.5px;line-height:1.45;color:var(--grey);margin-top:2px}
  .feature__list li::before{content:"• "}
</style>
</head>
<body>

<!-- Front side -->
<article class="flyer flyer--front">
  <div class="hero-photo hero-photo--couple" role="img" aria-label="Smiling senior couple embracing"></div>
  <div class="bands" style="top:250px">
    <svg width="540" height="160" viewBox="0 0 540 160">
      <polygon points="0,0 540,110 540,160 0,160" fill="var(--paper)"/>
      <polygon points="0,20 540,110 540,125 0,45" fill="var(--green)"/>
      <polygon points="0,45 540,125 540,140 0,70" fill="var(--charcoal)"/>
      <polygon points="0,70 540,140 540,160 0,160" fill="var(--paper)"/>
    </svg>
  </div>
  <div class="brand" style="right:28px;top:130px">
    <span class="brand__mark"></span><span class="brand__name">Fennick Medical</span>
  </div>
  <div class="headline-save">
    <div class="headline-save__big">We Save</div>
    <div class="headline-save__sub">The patient, time and money every month</div>
  </div>
  <h2 class="intro">We are a pharmacy that specializes in diabetic testing supplies and diabetic oral medications.</h2>
  <div class="photo-row">
    <div class="photo photo--pharmacist" role="img" aria-label="Pharmacist at the counter in a pharmacy"></div>
    <div class="photo photo--test" role="img" aria-label="Blood sugar test on a fingertip with a meter"></div>
  </div>
  <p class="body-copy">Just give us a call or fill out our form online on our secure website. We do the rest. We first research your insurance to maximize your benefits. Once we know what will save you the most money we contact your physician and get the correct prescription. Then it arrives on your doorstep.</p>
  <footer class="footer">
    <span class="footer__item"><svg viewBox="0 0 24 24"><path d="M6.6 10.8a15 15 0 006.6 6.6l2.2-2.2a1 1 0 011-.25 11.4 11.4 0 003.6.57 1 1 0 011 1V20a1 1 0 01-1 1A17 17 0 013 4a1 1 0 011-1h3.5a1 1 0 011 1c0 1.25.2 2.45.57 3.6a1 1 0 01-.25 1z"/></svg>(855) 555-0143</span>
    <span class="footer__item"><svg viewBox="0 0 24 24"><circle cx="12" cy="12" r="10"/></svg>www.fennickmedical.net</span>
    <span class="footer__item"><svg viewBox="0 0 24 24"><path d="M2 5h20v14H2z M2 5l10 8 10-8" /></svg>fennickmed@mail.com</span>
  </footer>
</article>

<!-- Back side -->
<article class="flyer flyer--back">
  <div class="hero-photo hero-photo--woman" role="img" aria-label="Worried woman reading a bill"></div>
  <div class="bands" style="top:270px">
    <svg width="540" height="130" viewBox="0 0 540 130">
      <polygon points="0,0 540,90 540,130 0,130" fill="var(--paper)"/>
      <polygon points="0,10 540,90 540,102 0,32" fill="var(--green)"/>
      <polygon points="0,32 540,102 540,114 0,54" fill="var(--charcoal)"/>
      <polygon points="0,54 540,114 540,130 0,130" fill="var(--paper)"/>
    </svg>
  </div>
  <div class="brand" style="left:30px;top:50px">
    <span class="brand__mark"></span><span class="brand__name">Fennick Medical</span>
  </div>
  <h2 class="question">
    <span class="question__lead">Are the costs of your</span><br>
    <span class="question__accent">Diabetic testing supplies</span><br>
    <span class="question__big">As high as your blood sugar?</span>
  </h2>
  <svg class="gift-badge" viewBox="0 0 130 130" aria-label="$20 gift card of your choice with your first order">
    <polygon fill="var(--green)" points="65,2 74,16 89,7 92,24 109,21 106,38 123,41 114,56 128,65 114,74 123,89 106,92 109,109 92,106 89,123 74,114 65,128 56,114 41,123 38,106 21,109 24,92 7,89 16,74 2,65 16,56 7,41 24,38 21,21 38,24 41,7 56,16"/>
    <circle cx="65" cy="65" r="44" fill="none" stroke="#fff" stroke-width="1.5"/>
    <text x="65" y="60" text-anchor="middle" font-family="Oswald,sans-serif" font-weight="600" font-size="28" fill="#fff">$20</text>
    <text x="65" y="76" text-anchor="middle" font-family="Oswald,sans-serif" font-size="12" fill="#fff">GIFT CARD</text>
    <text x="65" y="89" text-anchor="middle" font-family="Open Sans,sans-serif" font-size="8" fill="#fff">of your choice with</text>
    <text x="65" y="99" text-anchor="middle" font-family="Open Sans,sans-serif" font-size="8" fill="#fff">your first order</text>
  </svg>

  <ul class="features">
    <li class="feature">
      <span class="feature__icon"><svg viewBox="0 0 50 50"><rect x="6" y="18" width="38" height="10" fill="var(--green)"/><rect x="9" y="30" width="32" height="16" fill="var(--green)"/><rect x="22" y="18" width="6" height="28" fill="#fff"/><path d="M25 18c-4-8-13-8-11-2s11 2 11 2c0 0 9 4 11-2s-7-6-11 2z" fill="none" stroke="var(--green)" stroke-width="3"/></svg></span>
      <div>
        <h3 class="feature__title">Free meter and gift card</h3>
        <ul class="feature__list">
          <li>We give you the meter that is right for you • Several meters to choose</li>
          <li>With your first order receive a $20 gift card of your choice</li>
          <li>Choose from Brightmart, ShopNova, or ValueHub.</li>
        </ul>
      </div>
    </li>
    <li class="feature">
      <span class="feature__icon"><svg viewBox="0 0 50 50"><circle cx="25" cy="25" r="21" fill="none" stroke="var(--green)" stroke-width="4"/><text x="25" y="34" text-anchor="middle" font-family="Oswald,sans-serif" font-weight="600" font-size="26" fill="var(--green)">$</text></svg></span>
      <div>
        <h3 class="feature__title">Save money</h3>
        <ul class="feature__list">
          <li>We research your insurance to maximize your benefits</li>
          <li>We save you the greatest amount of money</li>
          <li>Save on out-of-pocket costs (copays) with every fill</li>
        </ul>
      </div>
    </li>
    <li class="feature">
      <span class="feature__icon"><svg viewBox="0 0 50 50"><circle cx="25" cy="27" r="18" fill="none" stroke="var(--green)" stroke-width="4"/><path d="M25 16v11l8 5" fill="none" stroke="var(--green)" stroke-width="4"/><path d="M6 12l8-7M44 12l-8-7" stroke="var(--green)" stroke-width="4"/></svg></span>
      <div>
        <h3 class="feature__title">Save time</h3>
        <ul class="feature__list">
          <li>Never wait in line again</li>
          <li>No driving to the pharmacy to get your prescriptions.</li>
        </ul>
      </div>
    </li>
    <li class="feature">
      <span class="feature__icon"><svg viewBox="0 0 50 50"><rect x="2" y="12" width="28" height="22" fill="var(--green)"/><path d="M32 18h9l7 8v8H32z" fill="var(--green)"/><circle cx="12" cy="38" r="5" fill="var(--green)" stroke="#fff" stroke-width="2"/><circle cx="39" cy="38" r="5" fill="var(--green)" stroke="#fff" stroke-width="2"/></svg></span>
      <div>
        <h3 class="feature__title">Free delivery, <em>right to your door</em></h3>
        <ul class="feature__list">
          <li>Never forget to pick up your prescriptions</li>
          <li>They arrive on your doorstep monthly</li>
        </ul>
      </div>
    </li>
  </ul>

  <footer class="footer">
    <span class="footer__item"><svg viewBox="0 0 24 24"><path d="M6.6 10.8a15 15 0 006.6 6.6l2.2-2.2a1 1 0 011-.25 11.4 11.4 0 003.6.57 1 1 0 011 1V20a1 1 0 01-1 1A17 17 0 013 4a1 1 0 011-1h3.5a1 1 0 011 1c0 1.25.2 2.45.57 3.6a1 1 0 01-.25 1z"/></svg>(855) 555-0143</span>
    <span class="footer__item"><svg viewBox="0 0 24 24"><circle cx="12" cy="12" r="10"/></svg>www.fennickmedical.net</span>
    <span class="footer__item"><svg viewBox="0 0 24 24"><path d="M2 5h20v14H2z M2 5l10 8 10-8" /></svg>fennickmed@mail.com</span>
  </footer>
</article>

</body>
</html>
```